Web design for Zembrolia.com

We need a website (4 starter pages) designed for a drupal based site. The theme is flexible so I am open to different designs/looks. I am looking for a VERY simple and clean and FUN design to make it easy to use for the customer.

Our company is similar to Kelvo pact as in it's for multiple people to design a cake for a customer and they choose a winning design and work with that cake designer to make the cake (birthday, wedding etc...)

Our vision:
First page:
2 main images for either the customer to submit an idea for a cake, or the new designer to sign up to the site. Perhaps a mouse-over with wording on what the options are? You can use this site:
http://www.plindorfy.com/ as a sort of template but more clean and simple

"How it works" page:
Similar to this:
http://www.plindorfy.com/how-it-works
Fun, clean and simple

Submit cake design page (form submission)

Submit new designer page

Ideally a 960 wide design with no flash, but open to a flash design if it stands out...

Please contact me if you have any questions!

People who want a custom cake made, and people who design and make cakes.

Wedding

• Use the logo attached. The "Oven Mit" should be a big part of the site...kind of a site mascot?
• 960 wide
No flash but not a deal-breaker if there is flash and it's amazing...

```html
<!DOCTYPE html>
<html lang="en">
<head>
<meta charset="utf-8">
<title>Zembrolia.com</title>
<link rel="stylesheet" href="https://fonts.googleapis.com/css2?family=Fredoka:wght@500;600&family=Ubuntu:wght@400;500;700&display=swap">
<style>
  :root {
    --backdrop: #563c31;
    --paper: #f3eee6;
    --paper-stripe: #ece6dc;
    --frame: #a8948b;
    --frame-light: #d8ccc4;
    --cocoa: #5b3f33;
    --cocoa-deep: #3b261e;
    --body-text: #6e5a52;
    --teal: #5aaaa8;
    --teal-dark: #3f8c8b;
    --teal-light: #8cc8c4;
    --pink: #e6a3b8;
    --pink-light: #f6dbe4;
    --footer: #4a3229;
    --footer-text: #b8a69c;
    --white: #ffffff;
  }
  * { box-sizing: border-box; margin: 0; padding: 0; }
  html, body { width: 1200px; height: 1200px; overflow: hidden; }
  body {
    background: var(--backdrop);
    font-family: "Ubuntu", sans-serif;
    position: relative;
  }
  .page {
    position: absolute;
    left: 112px; top: 49px;
    width: 976px; height: 1151px;
    background:
      repeating-linear-gradient(90deg, var(--paper) 0 75px, var(--paper-stripe) 75px 150px);
    border: 4px solid var(--frame);
    border-bottom: none;
    border-radius: 28px 28px 0 0;
    box-shadow: inset 0 0 0 6px var(--paper), inset 0 0 0 8px var(--frame-light);
  }
  .brand {
    position: absolute; left: 158px; top: 104px;
    display: flex; align-items: center; gap: 12px;
  }
  .brand-dot {
    width: 58px; height: 58px; border-radius: 50%;
    background: var(--pink);
  }
  .brand-name {
    font-family: "Fredoka", sans-serif; font-weight: 600;
    font-size: 44px; color: var(--cocoa); letter-spacing: -1px;
  }
  .main-nav {
    position: absolute; left: 668px; top: 126px;
    width: 434px; height: 30px;
    background: var(--teal);
    display: flex; align-items: center;
    padding-left: 26px;
    clip-path: polygon(0 0, 100% 0, 96% 50%, 100% 100%, 0 100%, 3% 50%);
  }
  .main-nav a {
    color: var(--white); text-decoration: none;
    font-size: 11.5px; font-weight: 500; letter-spacing: 1.6px;
    padding: 0 11px; line-height: 30px;
    border-right: 1px dashed rgba(255,255,255,.6);
  }
  .main-nav a.is-current { background: var(--teal-dark); font-weight: 700; }
  .main-nav .help {
    margin-left: 10px; background: var(--white); color: var(--teal-dark);
    border-radius: 3px; padding: 0 8px; line-height: 15px; font-weight: 700; border: none;
  }
  .hero-frame {
    position: absolute; left: 98px; top: 198px;
    width: 1004px; height: 336px;
    background: var(--paper);
    box-shadow: 0 2px 4px rgba(0,0,0,.25);
  }
  .hero-photo {
    position: absolute; left: 15px; top: 14px;
    width: 974px; height: 307px;
    background: radial-gradient(ellipse at 52% 50%, #6a4636 0%, #4a2f24 55%, var(--cocoa-deep) 100%);
  }
  .hero-line {
    position: absolute; color: var(--white);
    font-family: "Fredoka", sans-serif; font-weight: 500;
    font-size: 27px; line-height: 27px;
  }
  .hero-line.lead { left: 52px; top: 74px; }
  .hero-line.follow { right: 36px; top: 214px; text-align: right; }
  .column {
    position: absolute; top: 565px; width: 410px;
    color: var(--body-text); font-size: 14px; line-height: 22.5px;
  }
  .column.contest { left: 158px; }
  .column.designer { left: 630px; }
  .column h2 {
    text-align: center; font-size: 19px; font-weight: 700;
    letter-spacing: 2.5px; color: var(--cocoa); margin-bottom: 25px;
    text-shadow: 1px 1px 0 var(--white);
  }
  .column p { margin-bottom: 22px; }
  .divider {
    position: absolute; left: 600px; top: 553px; height: 368px;
    border-left: 2px dotted var(--cocoa);
  }
  .start-badge { position: absolute; left: 296px; top: 808px; }
  .signup {
    position: absolute; left: 779px; top: 845px;
    width: 92px; height: 20px; border-radius: 3px;
    background: #d7cdc5; border: 1px solid var(--frame);
    color: var(--cocoa); font-size: 10.5px; font-weight: 700;
    letter-spacing: 1.5px; text-align: center; line-height: 18px;
  }
  .gingham {
    position: absolute; left: 112px; top: 940px; width: 976px; height: 45px;
    background: linear-gradient(180deg, var(--pink-light), var(--pink));
  }
  .footer {
    position: absolute; left: 112px; top: 985px; width: 976px; height: 215px;
    background: var(--footer);
  }
  .footer-list {
    position: absolute; top: 27px; list-style: none;
    font-size: 12px; line-height: 18.8px; color: var(--footer-text);
  }
  .footer-list.categories { left: 46px; }
  .footer-list.site { left: 197px; }
  .footer-list.legal { left: 346px; }
  .social { position: absolute; right: 46px; top: 17px; display: flex; gap: 6px; }
  .social span { width: 24px; height: 24px; border-radius: 50%; background: var(--teal-light); }
  .copyright {
    position: absolute; right: 44px; top: 65px; text-align: right;
    font-size: 12px; line-height: 18.8px; color: var(--footer-text);
  }
</style>
</head>
<body>
  <div class="page"></div>

  <header>
    <div class="brand">
      <span class="brand-dot"></span>
      <span class="brand-name">Zembrolia.com</span>
    </div>
    <nav class="main-nav">
      <a class="is-current">HOME</a><a>BROWSE</a><a>TOUR</a><a>CONTACT</a><a>LOG IN</a><a class="help">?</a>
    </nav>
  </header>

  <section class="hero-frame">
    <div class="hero-photo" role="img" aria-label="Smiling baker in a pink apron holding up pink oven mitts, surrounded by sketched cakes and cupcakes on a chocolate brown background"></div>
    <p class="hero-line lead">Submit your dream<br>cake’s desire ....</p>
    <p class="hero-line follow">.... and receive<br>proposition from all<br>over the world !</p>
  </section>

  <main>
    <section class="column contest">
      <h2>CONTEST HOLDERS</h2>
      <p>Lorem ipsum do pland sit amet, con sectetur a dip sching elit.</p>
      <p>I ped diam non nu my e plusmode tempor in cidunt ut labore et dolore. Oh magna alip quam erat volu pat.</p>
      <p>Ut dernime ad minim veniam, quis no strud exercit libration ullamcorper suscipit lab oris nisi ut aliquip ex ea commodo consequat.</p>
    </section>
    <div class="divider"></div>
    <section class="column designer">
      <h2>CAKE DESIGNER</h2>
      <p>Duis autem vel eum irure dolor in reprehendert in voluptate velit esse molestaie consequat, vel illum dolore eu fugiat nulla pariatur.</p>
      <p>At vero eos et accusam et iusto odio blandit praesent lup-tatum delenit aigue duos dolor et molestias exceptur sint dupic non provident, simil tempor sunt in culpa qui deserunt mollit anim id est laborum et dolor fup.</p>
    </section>

    <svg class="start-badge" width="156" height="92" viewBox="0 0 156 92">
      <polygon points="0,36 40,36 40,66 0,66 12,51" fill="#4f9e9c"/>
      <polygon points="156,36 116,36 116,66 156,66 144,51" fill="#4f9e9c"/>
      <circle cx="78" cy="46" r="44" fill="#6cb5b2"/>
      <circle cx="78" cy="46" r="38" fill="none" stroke="#ffffff" stroke-opacity=".35" stroke-width="1.5"/>
      <text x="78" y="55" text-anchor="middle" font-family="Fredoka, sans-serif" font-weight="600" font-size="27" fill="#ffffff">Start</text>
    </svg>
    <div class="signup">SIGN-UP</div>
  </main>

  <div class="gingham" role="img" aria-label="Pink and white gingham ribbon band with zigzag edges"></div>

  <footer class="footer">
    <ul class="footer-list categories">
      <li>Wedding cakes</li><li>Birthday cakes</li><li>Christening cakes</li><li>Creative cakes</li><li>Celebration cakes</li><li>Special event</li>
    </ul>
    <ul class="footer-list site">
      <li>Home</li><li>Browse</li><li>Tour</li><li>Contact</li><li>Log In</li>
    </ul>
    <ul class="footer-list legal">
      <li>User agreement</li><li>Privacy policy</li><li>Sitemap</li>
    </ul>
    <div class="social"><span></span><span></span></div>
    <p class="copyright">© Copyright 2012<br>Zembrolia.com</p>
  </footer>
</body>
</html>
```